Powerpoint presentation about personal finance

Investing 4$ per day is what has been required to become a millionaire by investing in the stock market from 1965 to 2015. Yet only 1% of the population is millionaire. This presentation is about the most common causes why people do not build significant wealth through their life. We intend to educate people with this presentation, but also build trust so they become client of our wealth management firm. Feel free to send us any question about this project.
Updates

Reason: I have uploaded the logo source file and an updated PPT file. Thanks

Target Market(s)

People with a willingness to save money between the age of 20 to 50 years old

Industry/Entity Type

Finance

Font styles to use
Sans Serif

Requirements
Must have
• We are looking at uniforming the design throughout the presentation with nice, classic tone colors, large font size as it needs to be visible 3 meters apart. The content of the presentation will be updated regularly.
Should not have
• cartoon style, not serious

```html
<!DOCTYPE html>
<html lang="fr">
<head>
<meta charset="utf-8">
<title>Présentation – finances personnelles</title>
<link href="https://fonts.googleapis.com/css2?family=Bebas+Neue&family=Carlito:ital,wght@0,400;0,700;1,400;1,700&display=swap" rel="stylesheet">
<style>
:root{
  --board:#7a1d1d;
  --title:#f1dede;
  --tray:#d9d9d9;
  --paper:#ffffff;
  --ink:#111111;
  --muted:#6b6b6b;
  --accent-blue:#1f4e99;
  --brand:#2a5aa8;
  --alert:#d81e1e;
  --grid:#d9d9d9;
  --line:#4f81bd;
}
*{box-sizing:border-box;margin:0;padding:0}
html,body{width:1200px;height:1200px;overflow:hidden}
body{background:var(--board);font-family:"Carlito",Calibri,sans-serif;color:var(--ink);position:relative}
.board-title{position:absolute;top:40px;left:0;width:1200px;text-align:center;font-family:"Bebas Neue",sans-serif;font-size:96px;letter-spacing:1px;color:var(--title);line-height:1}
.tray{position:absolute;left:11px;top:195px;width:1174px;height:946px;background:var(--tray)}
.slide{position:absolute;width:280px;height:210px;background:var(--paper);overflow:hidden}
.num{position:absolute;font-size:9px;font-weight:700;color:#333}
.brand{position:absolute;top:6px;right:20px;display:flex;align-items:center;gap:3px;font-size:9px;font-weight:700;color:var(--brand)}
.brand .dot{width:14px;height:14px;border-radius:50%;border:1.5px solid var(--brand)}
.rule{position:absolute;left:12px;right:18px;height:1.5px;background:linear-gradient(90deg,#3a6fc4,#9b3bb5,#d9342b,#f0a21b,#3faa48,#3a6fc4,#9b3bb5,#d9342b)}
.rule.top{top:26px}
.rule.bottom{bottom:18px}
.heading{position:absolute;top:12px;left:14px;font-size:12px;color:#7b7b7b}
.body{position:absolute;left:20px;right:20px}
.caps{font-variant:small-caps;font-weight:700;font-size:14px;line-height:1.45;text-align:justify}
.center{text-align:center}
ul.list{list-style:none}
ul.list li{position:relative;padding-left:16px;font-size:7.5px;line-height:1.3;text-align:justify}
ul.list li::before{content:"•";position:absolute;left:2px}
.small{font-size:7.5px;line-height:1.35}
.blue{color:var(--accent-blue)}
.red{color:var(--alert)}
.b{font-weight:700}
.i{font-style:italic}
svg{display:block}
</style>
</head>
<body>
<h1 class="board-title">Powerpoint Design Idea - 01</h1>
<div class="tray"></div>

<!-- Row 1 -->
<div class="slide" style="left:14px;top:198px">
  <div class="brand"><span class="dot"></span>NOVALIS</div><div class="rule top"></div>
  <p class="body caps" style="top:66px;font-size:13px">L’idéal pour nous tous n’est-il pas d’avoir suffisamment d’argent et d’être en santé afin de pouvoir réaliser nos rêves?</p>
  <div class="rule bottom"></div>
</div><span class="num" style="left:286px;top:414px">1</span>

<div class="slide" style="left:310px;top:198px">
  <div class="brand"><span class="dot"></span>NOVALIS</div><div class="rule top"></div>
  <p class="body caps center" style="top:88px">Quels sont vos rêves?</p>
  <div class="rule bottom"></div>
</div><span class="num" style="left:582px;top:414px">2</span>

<div class="slide" style="left:606px;top:198px">
  <div class="brand"><span class="dot"></span>NOVALIS</div><div class="rule top"></div>
  <p class="body caps" style="top:52px;font-size:13.5px">Malheureusement, ce n’est pas tout le monde qui ont la chance de réaliser tous leurs rêves, pourtant ceci est à la portée de presque tous…</p>
  <div class="rule bottom"></div>
</div><span class="num" style="left:878px;top:414px">3</span>

<div class="slide" style="left:902px;top:198px">
  <p class="body center red" style="top:14px;font-size:6.5px;line-height:1.3">Investissement fixe équivalent à <u>4$ par jour</u> dans les actions pour un individu né en 1950 et qui a commencé à épargner à 15 ans</p>
  <svg style="position:absolute;left:8px;top:44px" width="266" height="160" viewBox="0 0 266 160">
    <g stroke="var(--grid)" stroke-width=".6"><line x1="30" y1="10" x2="260" y2="10"/><line x1="30" y1="34" x2="260" y2="34"/><line x1="30" y1="58" x2="260" y2="58"/><line x1="30" y1="82" x2="260" y2="82"/><line x1="30" y1="106" x2="260" y2="106"/><line x1="30" y1="130" x2="260" y2="130"/><line x1="30" y1="148" x2="260" y2="148"/></g>
    <g font-size="3.5" fill="#555" text-anchor="end"><text x="26" y="12">1 200 000 $</text><text x="26" y="36">1 000 000 $</text><text x="26" y="60">800 000 $</text><text x="26" y="84">600 000 $</text><text x="26" y="108">400 000 $</text><text x="26" y="132">200 000 $</text><text x="26" y="150">0 $</text></g>
    <ellipse cx="18" cy="34" rx="11" ry="5" fill="none" stroke="var(--alert)" stroke-width=".8"/>
    <polyline fill="none" stroke="var(--line)" stroke-width="1" points="32,148 60,147 90,146 120,145 140,143 155,140 170,136 180,130 190,126 200,120 208,112 214,100 220,82 226,70 232,86 236,96 242,76 248,74 254,56 258,48 262,30 266,20"/>
    <line x1="32" y1="154" x2="260" y2="154" stroke="#888" stroke-width=".5" stroke-dasharray="1 1.5"/>
  </svg>
</div><span class="num" style="left:1174px;top:414px">4</span>

<!-- Row 2 -->
<div class="slide" style="left:14px;top:439px">
  <div class="brand"><span class="dot"></span>NOVALIS</div><div class="rule top"></div>
  <p class="body b" style="top:56px;font-size:12.5px;line-height:1.35">Pourquoi y a-t-il si peu de gens qui sont millionnaires aujourd’hui quand l’équivalent de 4$ par jour d’économies investis dans la bourse de 1950 à 2015 a généré un portefeuille de plus de 1 million de dollars?</p>
  <div class="rule bottom"></div>
</div><span class="num" style="left:286px;top:655px">5</span>

<div class="slide" style="left:310px;top:439px">
  <div class="heading">Le constat…</div>
  <div class="brand"><span class="dot"></span>NOVALIS</div><div class="rule top"></div>
  <ul class="list body" style="top:36px">
    <li>80% des familles québécoises ont accumulé moins de 300,000$ d’épargne.</li>
    <li style="margin-top:9px">C’est donc dire que la majorité des familles s’expose à une précarité financière.</li>
    <li style="margin-top:9px">L’industrie financière ne s’intéresse peu aux familles ayant moins de 250,000$ d’épargne parce qu’elle ne les trouve pas rentables.</li>
    <li style="margin-top:9px">L’industrie financière échoue donc dans son devoir d’assister les familles dans l’atteinte de leurs objectifs financiers.</li>
  </ul>
  <div class="rule bottom"></div>
</div><span class="num" style="left:582px;top:655px">6</span>

<div class="slide" style="left:606px;top:439px">
  <div class="heading">Notre projet</div>
  <div class="brand"><span class="dot"></span>NOVALIS</div><div class="rule top"></div>
  <p class="body b center" style="top:46px;font-size:12px;line-height:1.4">Notre projet, d’ordre social, est d’aider les familles à maximiser leur indépendance financière à long terme en partageant leur savoir et notre expertise.<br><br>Votre succès deviendra donc notre succès!</p>
  <div class="rule bottom"></div>
</div><span class="num" style="left:878px;top:655px">7</span>

<div class="slide" style="left:902px;top:439px">
  <div class="brand"><span class="dot"></span>NOVALIS</div><div class="rule top"></div>
  <p class="body small" style="top:40px">Les principaux facteurs qui nuisent à l’atteinte de l’indépendance financière:</p>
  <ul class="list body" style="top:72px">
    <li>L’inaction et le report à plus tard</li><li>Les erreurs émotives (la peur)</li><li>Favoriser les plaisirs à court terme plutôt que les bénéfices à long terme</li><li>Le manque de connaissances</li><li>L’accès à l’information</li><li>Les frais de gestion et la rémunération des conseiller financiers</li><li>Les impôts</li><li>L’inflation</li>
  </ul>
  <div class="rule bottom"></div>
</div><span class="num" style="left:1174px;top:655px">8</span>

<!-- Row 3 -->
<div class="slide" style="left:14px;top:677px">
  <div class="heading">L’inaction…</div>
  <div class="brand"><span class="dot"></span>NOVALIS</div><div class="rule top"></div>
  <p class="body blue small center" style="top:44px">Vous croyez ne pas avoir les moyens d’épargner?</p>
  <p class="body small" style="top:72px;left:16px">Pour générer 4$ par jour, il suffit:</p>
  <ul class="list body i" style="top:90px;left:16px">
    <li>faire son café à la maison au lieu de l’acheter sur la route</li>
    <li style="margin-top:8px">Faire son lunch au lieu de manger au restaurant</li>
    <li style="margin-top:8px">Réduire le nombre de chaînes sur votre abonnement au câble</li>
  </ul>
  <p class="body small" style="top:154px;left:16px">Bref il est possible d’y arriver sans réduire son style de vie de façon significative!</p>
  <div class="rule bottom"></div>
</div><span class="num" style="left:286px;top:893px">9</span>

<div class="slide" style="left:310px;top:677px">
  <div class="heading">L’inaction…</div>
  <div class="brand"><span class="dot"></span>NOVALIS</div><div class="rule top"></div>
  <p class="body blue small center" style="top:36px">Vous croyez que ce n’est pas utile d’épargner car vous pourriez mourir demain matin?</p>
  <p class="body small" style="top:68px">Vous avez cependant plus de risque d’avoir des ennuis financiers à cause de ces événements:</p>
  <ul class="list body i b" style="top:100px;left:20px">
    <li>Divorce</li><li>Perte d’emploi</li><li>Maladie grave</li><li>Réduction des prestations gouvernementales</li><li>Espérance de vie qui s’allonge</li>
  </ul>
  <p class="body small" style="top:168px">Avoir de l’épargne vous aiderait grandement à passer à travers ces dures épreuves…</p>
  <div class="rule bottom"></div>
</div><span class="num" style="left:578px;top:893px">10</span>

<div class="slide" style="left:606px;top:677px">
  <div class="heading">Les erreurs émotives (La peur)…</div>
  <div class="brand"><span class="dot"></span>NOVALIS</div><div class="rule top"></div>
  <ul class="list body" style="top:36px;left:14px">
    <li>En 1973 et 1974, la valeur des actions américaines diminue de 40%.</li>
    <li style="margin-top:9px">Un investisseur qui avait investi 100$ par mois depuis 1965 a vu son portefeuille passé de 13,300$ à 9,500$.</li>
    <li style="margin-top:9px">Pris de panique, il vend toutes ses actions pour arrêter l’hémorragie.</li>
    <li style="margin-top:9px">En 1975, les actions américaines augmentent de 37%. Maintenant tout excité après une telle performance, l’investisseur réinvesti ses 9,500$ l’année suivante.</li>
  </ul>
  <p class="body small center" style="top:180px">Quel a été l’impact de cette décision?</p>
  <div class="rule bottom"></div>
</div><span class="num" style="left:874px;top:893px">11</span>

<div class="slide" style="left:902px;top:677px">
  <p class="body center red b" style="top:14px;font-size:6.3px;line-height:1.3">Investissement fixe équivalent à 4$ par jour dans l’Indice 500 au cours des 50 dernières années mais avec le retrait total des investissements suite à la baisse de 40% de 1973/1974 et réinvestissement en 1976</p>
  <p style="position:absolute;left:36px;top:68px;font-size:6px;color:var(--accent-blue)">Cette décision provoquée par la peur a coûté 300,000$ !</p>
  <svg style="position:absolute;left:8px;top:52px" width="266" height="150" viewBox="0 0 266 150">
    <g stroke="var(--grid)" stroke-width=".6"><line x1="30" y1="8" x2="260" y2="8"/><line x1="30" y1="30" x2="260" y2="30"/><line x1="30" y1="52" x2="260" y2="52"/><line x1="30" y1="74" x2="260" y2="74"/><line x1="30" y1="96" x2="260" y2="96"/><line x1="30" y1="118" x2="260" y2="118"/><line x1="30" y1="138" x2="260" y2="138"/></g>
    <g font-size="3.5" fill="#555" text-anchor="end"><text x="26" y="10">1 200 000 $</text><text x="26" y="32">1 000 000 $</text><text x="26" y="54">800 000 $</text><text x="26" y="76">600 000 $</text><text x="26" y="98">400 000 $</text><text x="26" y="120">200 000 $</text><text x="26" y="140">0 $</text></g>
    <ellipse cx="18" cy="52" rx="11" ry="5" fill="none" stroke="var(--alert)" stroke-width=".8"/>
    <polyline fill="none" stroke="var(--line)" stroke-width="1" points="32,138 70,137 110,136 140,134 160,131 175,127 188,121 198,116 206,108 214,96 222,84 228,94 232,102 238,88 244,86 250,70 256,60 262,54"/>
    <line x1="32" y1="144" x2="260" y2="144" stroke="#888" stroke-width=".5" stroke-dasharray="1 1.5"/>
  </svg>
</div><span class="num" style="left:1170px;top:893px">12</span>

<!-- Row 4 -->
<div class="slide" style="left:14px;top:907px">
  <p class="body center red" style="top:10px;font-size:6.5px;line-height:1.3">Rendement annuel minimum, maximum et moyen de l’Indice 500 de 1935 à 2016</p>
  <svg style="position:absolute;left:8px;top:28px" width="266" height="178" viewBox="0 0 266 178">
    <g stroke="var(--grid)" stroke-width=".5"><line x1="26" y1="6" x2="262" y2="6"/><line x1="26" y1="30" x2="262" y2="30"/><line x1="26" y1="54" x2="262" y2="54"/><line x1="26" y1="78" x2="262" y2="78"/><line x1="26" y1="102" x2="262" y2="102"/><line x1="26" y1="126" x2="262" y2="126"/><line x1="26" y1="150" x2="262" y2="150"/></g>
    <g font-size="3.5" fill="#555" text-anchor="end"><text x="22" y="8">60,0%</text><text x="22" y="32">40,0%</text><text x="22" y="56">20,0%</text><text x="22" y="80">0,0%</text><text x="22" y="104">-20,0%</text><text x="22" y="128">-40,0%</text><text x="22" y="152">-60,0%</text></g>
    <g stroke="#333" stroke-width=".7">
      <line x1="40" y1="8" x2="40" y2="132"/><line x1="66" y1="22" x2="66" y2="110"/><line x1="92" y1="34" x2="92" y2="96"/><line x1="118" y1="40" x2="118" y2="92"/><line x1="144" y1="44" x2="144" y2="88"/><line x1="170" y1="50" x2="170" y2="84"/><line x1="196" y1="54" x2="196" y2="82"/><line x1="222" y1="58" x2="222" y2="80"/><line x1="244" y1="62" x2="244" y2="78"/><line x1="258" y1="66" x2="258" y2="76"/>
    </g>
    <g fill="#c8c83a"><circle cx="40" cy="68" r="1.3"/><circle cx="66" cy="68" r="1.3"/><circle cx="92" cy="68" r="1.3"/><circle cx="118" cy="68" r="1.3"/><circle cx="144" cy="68" r="1.3"/><circle cx="170" cy="68" r="1.3"/><circle cx="196" cy="68" r="1.3"/><circle cx="222" cy="68" r="1.3"/><circle cx="244" cy="68" r="1.3"/><circle cx="258" cy="68" r="1.3"/></g>
    <ellipse cx="40" cy="106" rx="7" ry="28" fill="none" stroke="var(--alert)" stroke-width=".8"/>
    <ellipse cx="196" cy="66" rx="6" ry="14" fill="none" stroke="var(--alert)" stroke-width=".8"/>
    <line x1="72" y1="14" x2="46" y2="74" stroke="var(--line)" stroke-width=".6"/>
    <line x1="210" y1="112" x2="200" y2="84" stroke="var(--line)" stroke-width=".6"/>
    <text x="72" y="8" font-size="4" fill="var(--accent-blue)">La peur de perdre de l’argent à court terme provoque</text>
    <text x="72" y="13" font-size="4" fill="var(--accent-blue)">de mauvaises décisions qui font finalement perdre</text>
    <text x="72" y="18" font-size="4" fill="var(--accent-blue)">beaucoup d’argent aux investisseurs…</text>
    <text x="190" y="118" font-size="4" fill="var(--accent-blue)">Les rendements sur une période de 15</text>
    <text x="190" y="123" font-size="4" fill="var(--accent-blue)">ans sont beaucoup plus stables et</text>
    <text x="190" y="128" font-size="4" fill="var(--accent-blue)">n’ont jamais été négatifs depuis 1935!</text>
    <g stroke="#999" stroke-width=".4" fill="none"><rect x="8" y="152" width="254" height="18"/><line x1="8" y1="158" x2="262" y2="158"/><line x1="8" y1="164" x2="262" y2="164"/></g>
    <g font-size="3" fill="#333"><text x="10" y="156.5">Minimum</text><text x="10" y="162.5">Maximum</text><text x="10" y="168.5">Moyenne</text></g>
  </svg>
</div><span class="num" style="left:282px;top:1123px">13</span>

<div class="slide" style="left:310px;top:907px">
  <div class="brand"><span class="dot"></span>NOVALIS</div><div class="rule top"></div>
  <ul class="list body" style="top:36px">
    <li>Chaque année, la firme américaine Veritan étudie les rendements réalisés par les investisseurs particuliers.</li>
    <li style="margin-top:9px">Ils constatent qu’au moment où le rendement moyen de actions au cours des trente dernières années a été de 10.35%, l’investisseur particulier a réalisé un rendement de 3.66% par année.</li>
    <li style="margin-top:9px">Ce résultat s’applique aux individus qui ont été conseillé par un professionnel.</li>
    <li style="margin-top:9px">Veritan attribue cette mauvaise performance en grande partie à la mauvaise gestion des émotions et en particulier la peur de perdre!</li>
  </ul>
  <div class="rule bottom"></div>
</div><span class="num" style="left:578px;top:1123px">14</span>

<div class="slide" style="left:606px;top:907px">
  <div class="brand"><span class="dot"></span>NOVALIS</div><div class="rule top"></div>
  <p class="body blue small" style="top:34px;left:16px">Favoriser les plaisirs à court terme plutôt que les bénéfices à long terme…</p>
  <p class="body small center" style="top:66px">Saviez-vous que l’équivalent de 4$ par jour investis à partir de l’âge de:</p>
  <ul class="list body" style="top:100px;left:16px">
    <li>15 ans aurait généré 2,000,000$ à 65 ans</li><li>25 ans aurait généré 700,000$ à 65 ans</li><li>35 ans aurait généré 250,000$ à 65 ans</li><li>45 ans aurait généré 90,000$ à 65 ans</li><li>55 ans aurait généré 25,000$ à 65ans</li>
  </ul>
  <p class="body small" style="top:172px;left:16px">Toujours repousser à plus tard la décision d’épargner coûte cher!</p>
  <div class="rule bottom"></div>
</div><span class="num" style="left:874px;top:1123px">15</span>

<div class="slide" style="left:902px;top:907px">
  <div class="heading">Le manque de connaissances…</div>
  <div class="brand"><span class="dot"></span>NOVALIS</div><div class="rule top"></div>
  <p class="body b" style="top:58px;font-size:9.5px">Dans quoi peut-on investir?</p>
  <div class="body" style="top:86px;font-size:9.5px;line-height:1.3">
    <p><span class="b" style="display:inline-block;width:22px">1.</span><b>Les obligations</b></p>
    <p style="padding-left:28px;font-size:7.5px" class="b">(rendement fixe mais faible)</p>
    <p style="margin-top:12px"><span class="b" style="display:inline-block;width:22px">2.</span><b>Les actions</b></p>
    <p style="padding-left:28px;font-size:7.5px" class="b">(rendement variable mais élevé)</p>
  </div>
  <div class="rule bottom"></div>
</div><span class="num" style="left:1170px;top:1123px">16</span>
</body>
</html>
```